Funeral Comparison Website Needs Designer For WireFrame Mock Up (That we've already done)

This should be a pretty quick design project. It's a single page based on a wireframe mockup we did.
Our site (restfulpathway.example) helps people find and compare funeral homes and cemeteries. Our site hasn't been redesigned since we launched in 2008, so it is fairly dated, and we've seen new competitors pop-up in the past year so we need to come up with a fresh redeisgn. We need someone to take our mockup and work their magic with it. As I mentioned this is a single page based on our wireframe mockup.
Please see attached mockup and logo.
Look and feel
Each slider illustrates characteristics of the customer's brand and the style your logo design should communicate.

```html
<!DOCTYPE html>
<html lang="en">
<head>
<meta charset="utf-8">
<title>Restful Pathway – Request Funeral Quotes</title>
<link href="https://fonts.googleapis.com/css2?family=Oswald:wght@400;500;700&family=Open+Sans:wght@400;600;700&family=Reenie+Beanie&display=swap" rel="stylesheet">
<style>
:root{
  --nav:#262626;
  --green:#57ad3c;
  --green-dark:#3f8f2a;
  --blue:#1f6ea6;
  --blue-card:#3d8fc9;
  --blue-card-text:#5aa6da;
  --blue-deep:#0f4d79;
  --ink:#2e3236;
  --grey-top:#f1f1f1;
  --grey-bottom:#cfd1d3;
  --support-bg:#e6e7e8;
  --footer:#2b2b2b;
  --footer-bottom:#1b1b1b;
  --muted:#8d8f91;
  --white:#ffffff;
}
*{box-sizing:border-box;margin:0;padding:0}
html,body{width:853px;height:1200px;overflow:hidden}
body{position:relative;font-family:"Open Sans",Arial,sans-serif;color:var(--ink);background:var(--support-bg)}
.abs{position:absolute}

/* nav */
.topbar{left:0;top:0;width:853px;height:24px;background:var(--nav)}
.menu{left:62px;top:0;display:flex;height:24px}
.menu a{color:#ddd;font-size:8px;font-weight:700;text-decoration:none;padding:0 10px;line-height:24px;letter-spacing:.3px}
.menu a.active{background:var(--green);color:var(--white)}
.call{right:120px;top:0;line-height:24px;font-size:9px;color:#ddd;font-weight:600}
.call b{color:var(--white)}
.social-dots{right:68px;top:6px;display:flex;gap:4px}
.social-dots span{width:12px;height:12px;border-radius:50%;background:var(--green)}

/* hero */
.hero{left:0;top:24px;width:853px;height:332px;background:linear-gradient(var(--grey-top),var(--grey-bottom))}
.brand{left:0;top:44px;width:853px;display:flex;justify-content:center;align-items:center;gap:8px}
.brand-mark{width:16px;height:16px;border-radius:50%;background:var(--green)}
.brand-name{font-weight:700;font-size:20px;color:var(--blue)}
.headline{left:0;top:104px;width:853px;text-align:center;font-family:"Oswald",sans-serif;font-weight:700;font-size:50px;color:var(--ink);letter-spacing:.5px;line-height:1}
.subline{left:0;top:165px;width:853px;text-align:center;font-family:"Oswald",sans-serif;font-weight:500;font-size:22px;color:#4a4e52}
.choice{font-family:"Reenie Beanie",cursive;font-size:22px;line-height:.9;color:#3a4a58;transform:rotate(-8deg);text-align:center}
.choice-1{left:140px;top:228px;width:150px}
.choice-2{left:330px;top:228px;width:160px}
.choice-3{left:520px;top:236px;width:130px}
.or{width:22px;height:22px;border-radius:50%;background:#9a9c9f;color:var(--white);font-size:8px;font-weight:700;display:flex;align-items:center;justify-content:center}
.or-1{left:300px;top:256px}
.or-2{left:498px;top:256px}
.figure{left:645px;top:92px;width:80px;height:264px;background:linear-gradient(#9c9fa3,#6f7276);border-radius:30px 30px 6px 6px;opacity:.85}

/* testimonials */
.testimonials{left:0;top:356px;width:853px;height:286px;background:var(--blue)}
.section-title-light{left:0;top:368px;width:853px;text-align:center;font-family:"Oswald",sans-serif;font-weight:500;font-size:28px;color:var(--white);letter-spacing:1px}
.title-rule{left:136px;top:412px;width:583px;height:1px;background:rgba(255,255,255,.35)}
.card{top:420px;width:185px;height:190px;background:var(--blue-card);border-radius:3px}
.card-1{left:136px}.card-2{left:335px}.card-3{left:534px}
.card p{position:absolute;left:8px;top:8px;right:8px;height:110px;background:var(--blue-card-text);padding:8px;font-size:9px;line-height:1.35;color:var(--white)}
.card .who{position:absolute;left:12px;top:138px;color:var(--white);font-size:12px;font-weight:700}
.card .who small{display:block;font-size:8px;font-weight:400}
.avatar{position:absolute;right:14px;top:128px;width:44px;height:44px;border-radius:50%;background:linear-gradient(#d9dde1,#8f99a3);border:2px solid var(--white)}
.arrow{top:504px;width:20px;height:20px;border-radius:50%;background:var(--blue-deep)}
.arrow-left{left:108px}.arrow-right{left:727px}

/* buttons */
.btn{top:660px;width:185px;height:42px;color:var(--white);font-weight:700;font-size:11px;display:flex;align-items:center;justify-content:center;text-align:center;line-height:1.2;border-radius:2px}
.btn-green{left:136px;background:var(--green)}
.btn-blue{background:var(--blue-deep)}
.btn-2{left:335px}.btn-3{left:534px}

/* support */
.section-title-dark{left:0;top:736px;width:853px;text-align:center;font-family:"Oswald",sans-serif;font-weight:500;font-size:28px;color:var(--ink);letter-spacing:1px}
.support-card{top:794px;width:185px;height:196px;background:var(--white);text-align:center;padding-top:12px}
.support-1{left:136px}.support-2{left:335px}.support-3{left:534px}
.support-card h3{font-family:"Oswald",sans-serif;font-weight:700;font-size:15px;color:var(--green);line-height:1.1}
.big-qa{font-family:"Oswald",sans-serif;font-size:38px;margin-top:10px;color:var(--ink)}
.support-card ul{list-style:none;text-align:left;padding-left:24px;margin-top:18px;font-size:9px;line-height:1.6}
.support-card ul li::before{content:"› ";color:var(--green);font-weight:700}
.support-card .note{font-size:9px;padding:0 26px;margin-top:14px;line-height:1.4}
.support-card svg{margin-top:12px}

/* footer */
.footer{left:0;top:1012px;width:853px;height:158px;background:var(--footer)}
.fcol{top:1030px;color:var(--muted);font-size:8px;line-height:1.7}
.fcol h4{color:#cfcfcf;font-size:9px;margin-bottom:4px}
.fcol-1{left:136px}.fcol-2{left:335px}.fcol-3{left:580px}
.fsocial{display:flex;align-items:center;gap:6px;margin-bottom:6px}
.fsocial span{width:14px;height:14px;border-radius:50%;background:#555}
.footer-bottom{left:0;top:1170px;width:853px;height:30px;background:var(--footer-bottom);color:#777;font-size:8px;line-height:30px;padding-left:136px}
</style>
</head>
<body>
<div class="abs topbar"></div>
<nav class="abs menu"><a class="active">HOME</a><a>HOW IT WORKS</a><a>ABOUT US</a><a>CONTACT US</a><a>RESOURCES</a></nav>
<div class="abs call">Give us a call: <b>800 555 0142</b></div>
<div class="abs social-dots"><span></span><span></span></div>

<header class="abs hero"></header>
<div class="abs brand"><span class="brand-mark"></span><span class="brand-name">restfulpathway.example</span></div>
<h1 class="abs headline">REQUEST FUNERAL QUOTES</h1>
<div class="abs subline">Free No Obligations Price &amp; Services Quotes</div>
<div class="abs choice choice-1">I am Planning for the Long Term Future</div>
<div class="abs or or-1">OR</div>
<div class="abs choice choice-2">I am Planning for a Death that will Occur Shortly</div>
<div class="abs or or-2">OR</div>
<div class="abs choice choice-3">A Death has just Occurred</div>
<div class="abs figure" role="img" aria-label="Silhouette of a man in a suit standing"></div>

<section class="abs testimonials"></section>
<h2 class="abs section-title-light">TESTIMONIALS</h2>
<div class="abs title-rule"></div>
<div class="abs card card-1"><p>Lorem ipsum dolor sit amet, consectetur adipiscing elit. Aenean massa cum sociis natoque penatibus et magnis dis parturient montes, nascetur ridiculus mus. Donec quam.</p><div class="who">John<small>Los Angeles CA</small></div><div class="avatar" role="img" aria-label="Customer portrait"></div></div>
<div class="abs card card-2"><p>Lorem ipsum dolor sit amet, consectetur adipiscing elit. Aenean massa cum sociis natoque penatibus et magnis dis parturient montes, nascetur ridiculus mus. Donec quam.</p><div class="who">John<small>Los Angeles CA</small></div><div class="avatar" role="img" aria-label="Customer portrait"></div></div>
<div class="abs card card-3"><p>Lorem ipsum dolor sit amet, consectetur adipiscing elit. Aenean massa cum sociis natoque penatibus et magnis dis parturient montes, nascetur ridiculus mus. Donec quam.</p><div class="who">John<small>Los Angeles CA</small></div><div class="avatar" role="img" aria-label="Customer portrait"></div></div>
<svg class="abs arrow arrow-left" viewBox="0 0 20 20"><path d="M12 5 L7 10 L12 15" fill="none" stroke="#fff" stroke-width="2"/></svg>
<svg class="abs arrow arrow-right" viewBox="0 0 20 20"><path d="M8 5 L13 10 L8 15" fill="none" stroke="#fff" stroke-width="2"/></svg>

<a class="abs btn btn-green">GET STARTED<br>WITH PRE-PLANNING</a>
<a class="abs btn btn-blue btn-2">GET STARTED</a>
<a class="abs btn btn-blue btn-3">GET STARTED</a>

<h2 class="abs section-title-dark">SUPPORT CENTER</h2>
<div class="abs support-card support-1"><h3>QUESTIONS &amp;<br>ANSWERS</h3><div class="big-qa">Q&amp;A</div><ul><li>How we help</li><li>How this works</li></ul></div>
<div class="abs support-card support-2"><h3>RESOURCES</h3>
<svg width="56" height="56" viewBox="0 0 56 56"><path d="M12 28a16 16 0 0 1 28-10" fill="none" stroke="#2e3236" stroke-width="5"/><path d="M36 10 L44 18 L34 22 Z" fill="#2e3236"/><path d="M44 28a16 16 0 0 1-28 10" fill="none" stroke="#2e3236" stroke-width="5"/><path d="M20 46 L12 38 L22 34 Z" fill="#2e3236"/></svg>
<ul style="margin-top:8px"><li>Advice</li><li>Finances</li><li>Planning Guides</li></ul></div>
<div class="abs support-card support-3"><h3>GET MORE HELP</h3>
<svg width="52" height="52" viewBox="0 0 52 52"><rect x="3" y="3" width="46" height="46" rx="4" fill="none" stroke="#2e3236" stroke-width="3"/><text x="26" y="37" text-anchor="middle" font-family="Oswald, sans-serif" font-size="30" font-weight="700" fill="#2e3236">?</text></svg>
<div class="note">Learn about our Certified consultant</div></div>

<footer class="abs footer"></footer>
<div class="abs fcol fcol-1"><h4>Useful Links</h4>Home<br>How it Works<br>About Us<br>Contact Us<br>Resources</div>
<div class="abs fcol fcol-2"><h4>Contact Us</h4>Tel: +00 (800) 555 0142<br>Mob: +00 (800) 555 0178<br>Email: support@restfulpathway.example</div>
<div class="abs fcol fcol-3"><h4>Stay Connected</h4><div class="fsocial"><span></span>Newsfeed</div><div class="fsocial"><span></span>Community Page</div></div>
<div class="abs footer-bottom">© 2014 Restful Pathway. All rights reserved. &nbsp;|&nbsp; Privacy Policy &nbsp;|&nbsp; Terms &amp; Conditions</div>
</body>
</html>
```